dealcraftmentor.com - Podcast Guest Marketing E-Flyer PDF

Dear Designers:I am in need of an attractive and attention-getting layout and design for a three-page marketing flyer (commonly known as a media one sheet) that will be sent via e-mail, as PDF file, to various Podcast hosts to market me as a guest on their podcasts. I want the design of the document to "mirror" the design and branding on my parent dealcraftmentor.com website. I am providing ALL the edited and proofread copy and content - the designer just needs to create the design for this marketing document. I want an active PDF document and icons should be used for WorkLoop, Phone, E-mail , and website- with hyperlinks that connect accordingly. I need a fast turnaround.
Updates

Dear Designers - instead of using the photo in the project file of me speaking to the audience for the banner image - I thought it would be a better idea to make this marketing piece specific to Podcast Hosts. Therefore, an image such as the one in the link below would be good to use for a banner image. https://www.pixelvarnow.com/find?q=podcast+studio+photos&mode=img&ref=univ&id=Qm7TzRk2LwPa9XcNvB4eHyU8sDjF1gA5oE3iKtZ6bW0nMh&w=1377&h=804#pic=vrolapemxq3BcT:

Target Market(s)

This PDF document will be sent to 650 Podcast hosts in North America via a broadcast e-mail.

Font styles to use
Sans Serif

Colors
ec1f27
ffffff
000000
333333
9d9d9d

Requirements
Must have
• A three-page layout that is easy to navigate in PDF form.
• Proper font styles and sizes for key emphasis areas on the document/
• Consistent branding to mirror my dealcraftmentor.com parent website
• Must be easy for people to read
• Attention-getting design elements and layout
• Professional and sophisticated design
• Icons for contact information
Should not have
• Should not be cluttered and junky-looking.
• Should not use small font sizes that makes it difficult to read.
• If Podcast hosts are interested in having me as a guest - they will read the content as required on three-pages

```html
<!DOCTYPE html>
<html lang="en">
<head>
<meta charset="utf-8">
<title>Dealcraft Mentor – Podcast Guest One Sheet</title>
<link href="https://fonts.googleapis.com/css2?family=Open+Sans:wght@400;600;700&display=swap" rel="stylesheet">
<style>
:root{
  --red:#ec1f27;
  --white:#ffffff;
  --black:#000000;
  --ink:#333333;
  --grey:#9d9d9d;
  --backdrop:#b9b9b9;
  --footer:#2e2e2e;
}
*{margin:0;padding:0;box-sizing:border-box}
html,body{width:1200px;height:582px;overflow:hidden}
body{background:var(--backdrop);font-family:"Open Sans",Arial,sans-serif;color:var(--ink);position:relative}
.page{position:absolute;top:30px;width:372px;height:524px;background:var(--white);overflow:hidden}
.page--one{left:28px}
.page--two{left:416px}
.page--three{left:802px}

.brand{height:58px;display:flex;align-items:center;justify-content:center;gap:6px}
.brand__mark{width:18px;height:18px;background:var(--red)}
.brand__name{font-size:19px;font-weight:600;color:var(--ink);letter-spacing:-.3px}

.banner{position:absolute;top:58px;left:0;width:372px;height:158px;background:linear-gradient(160deg,#6b4a3f 0%,#3c3a3d 45%,#8a8d92 100%)}
.headshot{position:absolute;top:146px;left:36px;width:120px;height:120px;border-radius:50%;border:4px solid var(--white);background:radial-gradient(circle at 50% 40%,#c9a791,#4a4a55 70%)}
.hero{position:absolute;top:216px;left:0;width:372px;height:100px;background:var(--red);color:var(--white);text-align:right;padding:10px 32px 0 34px}
.hero__kicker{font-size:11.5px;font-weight:400}
.hero__name{font-size:18px;font-weight:700;line-height:1.15}
.hero__tag{font-size:12.5px;font-weight:700;text-align:left;margin-top:4px;margin-left:-0px;white-space:nowrap;margin-left:-2px}
.hero__lede{font-size:6.3px;text-align:left;margin-top:3px;line-height:1.4}

.content{position:absolute;left:36px;right:30px}
.heading{font-size:8.8px;font-weight:400;color:var(--black);margin-bottom:5px;position:relative;padding-bottom:6px}
.heading em{font-style:normal;font-weight:700;color:var(--red)}
.heading::after{content:"";position:absolute;left:0;bottom:0;width:12px;height:2px;background:var(--red)}
.heading--nobar::after{display:none}
.heading--big{font-size:9.5px}
.body{font-size:5.3px;line-height:1.5;margin-bottom:6px}
.body strong{color:var(--black)}

.reasons{position:relative;list-style:none}
.reasons::before{content:"";position:absolute;left:6px;top:-12px;bottom:-6px;width:1.5px;background:var(--red)}
.reason{position:relative;font-size:5.3px;line-height:1.5;margin-bottom:7px;min-height:16px;padding-left:25px}
.reason__num{position:absolute;left:-2px;top:0;width:16px;height:16px;border-radius:50%;background:var(--red);color:var(--white);font-size:6px;font-weight:700;display:flex;align-items:center;justify-content:center;border:2px solid #f7c9cb}

.footer{position:absolute;left:0;bottom:0;width:372px;height:26px;background:var(--footer);color:var(--white);font-size:7.8px;display:flex;align-items:center}
.footer__left{display:flex;gap:14px;padding-left:20px;flex:1}
.footer__right{position:relative;height:26px;width:150px;display:flex;align-items:center;padding-left:26px}
.footer__right svg.slant{position:absolute;left:0;top:0}
.footer__right span{position:relative;display:flex;align-items:center;gap:4px}
.contact{display:flex;align-items:center;gap:4px}

.media{display:flex;align-items:center;gap:8px;margin:6px 0 14px}
.outlet{display:flex;align-items:center;gap:3px;height:40px;padding:0 5px;border:1px solid #e2e2e2}
.outlet__box{width:8px;height:8px;background:var(--red)}
.outlet__name{font-size:8px;font-weight:700;color:var(--ink)}

.quote{position:relative;font-size:5.3px;line-height:1.5;padding:0 24px 0 18px;margin-bottom:8px}
.quote::before{content:"\201C";position:absolute;left:0;top:-6px;font-size:22px;color:#d6d6d6;font-weight:700}
.quote::after{content:"\201D";position:absolute;right:2px;bottom:-14px;font-size:22px;color:#d6d6d6;font-weight:700}
.quote--lead{font-size:5.8px;padding-left:26px}
.quote--lead::before,.quote--lead::after{font-size:38px;top:-10px}
.quote--lead::after{bottom:-26px;top:auto}
.cite{text-align:right;font-size:6px;font-weight:700;color:var(--black);padding-right:24px}
.cite span{display:block;color:var(--red)}

.more{position:absolute;right:20px;top:391px;height:20px;padding:0 16px;border-radius:10px;background:#2a2a2a;color:var(--white);font-size:6px;font-weight:700;display:flex;align-items:center;z-index:2}
.closer{position:absolute;left:0;bottom:0;width:372px;height:122px;background:var(--red);color:var(--white);padding:16px 0 0 32px}
.closer__org{font-size:10px;font-weight:700;line-height:1.3}
.closer__role{font-size:7px;line-height:1.4}
.closer__cta{font-size:10px;font-weight:700;margin-top:8px;white-space:nowrap}
.closer__row{display:flex;gap:20px;font-size:7.5px;margin-top:6px;align-items:center}
.closer__phone{font-size:13px;font-weight:700;margin-top:4px;display:flex;align-items:center;gap:5px}
.closer__site{position:absolute;right:0;bottom:0;width:190px;height:22px;display:flex;align-items:center;padding-left:42px;font-size:7.8px}
.closer__site svg{position:absolute;left:0;top:0}
.dots{position:absolute;right:36px;top:40px;display:flex;gap:4px}
.dots i{width:12px;height:12px;border-radius:50%;background:var(--white);opacity:.9;display:block}
</style>
</head>
<body>

<section class="page page--one">
  <header class="brand">
    <span class="brand__mark"></span>
    <span class="brand__name">dealcraftmentor</span>
  </header>
  <div class="banner" role="img" aria-label="Photo of the speaker presenting to a seated business audience in a conference room"></div>
  <div class="hero">
    <p class="hero__kicker">Meet Dealcraft Mentor®</p>
    <h1 class="hero__name">Daniel R. Whitcombe</h1>
    <p class="hero__tag">The Expert You Need As a Guest on Your Podcast</p>
    <p class="hero__lede">Are you looking for a relevant and appealing topic and an engaging subject matter expert who can provide measurable value and life-changing tips to the listeners of your podcast?</p>
  </div>
  <div class="headshot" role="img" aria-label="Portrait photo of Daniel R. Whitcombe in a suit"></div>

  <div class="content" style="top:328px">
    <h2 class="heading">Why Negotiating and Decision Making <em>Should Be Topics on Your Podcast</em></h2>
    <p class="body">Regardless of your podcast theme – it's important to remember that your listeners are negotiating all the time – in their personal lives, social lives, and especially in their business lives. Negotiating is an essential life skill. Everyone can improve his or her negotiating skills, and Daniel is the expert who can provide the answers your people crave. Your podcast listeners will benefit from Daniel's proven, practical, and relevant negotiating strategies and tips that will improve results and outcomes in all types of personal and business negotiations.</p>
    <h2 class="heading" style="margin-bottom:10px">Six Reasons to Book <em>Daniel R. Whitcombe As a Guest on Your Podcast</em></h2>
    <ol class="reasons">
      <li class="reason"><span class="reason__num">01</span>Daniel is a dynamic, thought-provoking, engaging, captivating, and entertaining speaker who will share some great personal stories to help your listeners better understand and relate to the topic of negotiating and decision-making dynamics. He will indeed challenge the "status quo."</li>
      <li class="reason"><span class="reason__num">02</span>Daniel is the founder of dealcraftmentor.com® and is an internationally recognized expert and highly rated speaker on the topics of negotiating and decision-making dynamics that affect negotiated outcomes. His versatility and commitment to proper preparation will ensure that his content is tailored to address the theme of your podcast and the needs of your listeners.</li>
    </ol>
  </div>

  <footer class="footer">
    <div class="footer__left">
      <span class="contact"><svg width="8" height="6" viewBox="0 0 8 6"><rect x=".5" y=".5" width="7" height="5" fill="none" stroke="#fff" stroke-width=".8"/><path d="M.5 .5 4 3.3 7.5 .5" fill="none" stroke="#fff" stroke-width=".8"/></svg>daniel@whitcombe-mail.com</span>
      <span class="contact"><svg width="7" height="7" viewBox="0 0 10 10"><circle cx="5" cy="5" r="4.3" fill="none" stroke="#fff"/><path d="M3.3 3c.3 1.8 1.5 3 3.4 3.6l.6-.9" fill="none" stroke="#fff"/></svg>555-014-2287</span>
    </div>
    <div class="footer__right">
      <svg class="slant" width="150" height="26" viewBox="0 0 150 26"><polygon points="8,0 150,0 150,26 0,26" fill="var(--white)"/><polygon points="14,0 150,0 150,26 6,26" fill="var(--red)"/></svg>
      <span><svg width="7" height="7" viewBox="0 0 10 10"><circle cx="5" cy="5" r="4.3" fill="none" stroke="#fff"/><path d="M.7 5h8.6M5 .7c-2.4 2.6-2.4 6 0 8.6M5 .7c2.4 2.6 2.4 6 0 8.6" fill="none" stroke="#fff" stroke-width=".8"/></svg>www.dealcraftmentor.com</span>
    </div>
  </footer>
</section>

<section class="page page--two">
  <div class="content" style="top:26px">
    <ol class="reasons">
      <li class="reason"><span class="reason__num">03</span>His five-star-rated presentations and training programs have been delivered around the world to small and medium-sized businesses, Top 500 corporations, and large industry, trade, and peer-to-peer associations such as Rising Leaders Council and Founders Circle.</li>
      <li class="reason"><span class="reason__num">04</span>Daniel has personally trained over 50,000 people of all experience levels, across multiple industries, in 31 countries how to negotiate more effectively.</li>
      <li class="reason"><span class="reason__num">05</span>With formal training in broadcasting and media arts, Daniel provides 30 years of experience as a professional speaker who can provide your listeners with valuable insights, solutions, and answers to address listeners' challenges and questions.</li>
      <li class="reason"><span class="reason__num">06</span>Daniel is the creator of the best-selling Deal Ready Toolkit Audio Learning Program – designed to be an effective all-in-one learning solution that helps people improve their negotiating capabilities and skills. He is also the host of his soon-to-be-launched Podcast – Deal Talk Daily.</li>
    </ol>
  </div>
  <div class="content" style="top:144px">
    <h2 class="heading heading--big">How Podcast <em>Listeners Will Benefit</em></h2>
    <p class="body">Most people are intimidated by the prospect and process of negotiating – and often view negotiating as an uncomfortable haggling and bargaining process that may involve confrontation, anxiety, and stress. If podcast listeners are like most people – then they probably are concerned about being taken advantage of – or that they are missing out on potential opportunities in their personal, social, and business negotiations.</p>
    <p class="body">To alleviate your listeners' concerns, Daniel will provide them with easy-to-understand negotiating strategies, tactics, phrases, and tips they can immediately apply – the moment the podcast episode ends. Your listeners will feel more confident when they are equipped with the powerful and beneficial strategies and techniques that will help them save/make money and arrive at better outcomes when negotiating with customers, clients, suppliers, contractors, financial institutions, retailers, co-workers, colleagues, and family members.</p>
    <h2 class="heading heading--big">Daniel R. Whitcombe <em>in the Media</em></h2>
    <p class="body"><strong>Daniel has appeared on radio programs, written articles or contributed to articles for the following media outlets:</strong></p>
    <div class="media">
      <div class="outlet"><span class="outlet__box"></span><span class="outlet__name">Northern Ledger</span></div>
      <div class="outlet"><span class="outlet__box"></span><span class="outlet__name">Market Weekly</span></div>
      <div class="outlet"><span class="outlet__box"></span><span class="outlet__name">Capital Review</span></div>
      <div class="outlet"><span class="outlet__box"></span><span class="outlet__name">Trade Forum</span></div>
    </div>
    <h2 class="heading heading--nobar heading--big" style="margin-bottom:0;padding-bottom:0">Three Ways You Can Profit</h2>
    <h2 class="heading heading--big"><em>From Booking Daniel R. Whitcombe on Your Podcast</em></h2>
    <p class="body"><strong>Upon mutual agreement, podcast hosts and listeners can have access to the following money-saving and profit-generating opportunities:</strong></p>
  </div>
  <div class="content" style="top:458px">
    <ol class="reasons">
      <li class="reason"><span class="reason__num">01</span>Podcast hosts will be provided with a specific promotional code to share with your listeners that will entitle them to receive a special one-time discount of $19.95US off the purchase of the MP3 download of the Deal Ready Toolkit Audio Learning Program available on my online store. Complete download and purchase instructions will be provided to podcast hosts to publish in your notes and also communicate to your listeners.</li>
    </ol>
  </div>
  <footer class="footer">
    <div class="footer__left">
      <span class="contact"><svg width="8" height="6" viewBox="0 0 8 6"><rect x=".5" y=".5" width="7" height="5" fill="none" stroke="#fff" stroke-width=".8"/><path d="M.5 .5 4 3.3 7.5 .5" fill="none" stroke="#fff" stroke-width=".8"/></svg>daniel@whitcombe-mail.com</span>
      <span class="contact"><svg width="7" height="7" viewBox="0 0 10 10"><circle cx="5" cy="5" r="4.3" fill="none" stroke="#fff"/><path d="M3.3 3c.3 1.8 1.5 3 3.4 3.6l.6-.9" fill="none" stroke="#fff"/></svg>555-014-2287</span>
    </div>
    <div class="footer__right">
      <svg class="slant" width="150" height="26" viewBox="0 0 150 26"><polygon points="8,0 150,0 150,26 0,26" fill="var(--white)"/><polygon points="14,0 150,0 150,26 6,26" fill="var(--red)"/></svg>
      <span><svg width="7" height="7" viewBox="0 0 10 10"><circle cx="5" cy="5" r="4.3" fill="none" stroke="#fff"/><path d="M.7 5h8.6M5 .7c-2.4 2.6-2.4 6 0 8.6M5 .7c2.4 2.6 2.4 6 0 8.6" fill="none" stroke="#fff" stroke-width=".8"/></svg>www.dealcraftmentor.com</span>
    </div>
  </footer>
</section>

<section class="page page--three">
  <div class="content" style="top:26px">
    <ol class="reasons">
      <li class="reason"><span class="reason__num">02</span>Podcast hosts will receive a 10% commission payable on the net sales dollar revenue generated from the sale of MP3 downloads of Daniel's Deal Ready Toolkit Audio Learning Program.</li>
      <li class="reason"><span class="reason__num">03</span>Podcast hosts will receive a 10% referral fee for any corporation or association that books Daniel for a presentation, seminar, or learning workshop that directly results from my participation on your podcast.</li>
    </ol>
    <p class="body" style="margin-top:6px">Note: Discount and commission payments are subject to agreement to standard terms and conditions.</p>
  </div>
  <div class="content" style="top:112px">
    <h2 class="heading heading--nobar heading--big" style="margin-bottom:0;padding-bottom:0">Testimonials:</h2>
    <h2 class="heading heading--big"><em>What Some Clients Are Saying About the Dealcraft Mentor®</em></h2>
    <p class="quote quote--lead" style="margin-top:8px">Daniel Whitcombe did a terrific job on my podcast. His negotiating insights and tips were well received by my listeners, and he was an engaging, knowledgeable, and entertaining guest. Given my expertise in real estate, I thought I was a good negotiator – until Daniel taught me a few new strategies and tips during the podcast. I would recommend Daniel to any podcast host – he is a pro and his topics are relevant and can benefit everyone.</p>
    <p class="cite">Gordon Pryce, Podcast Host<span>Property Builders Podcast, Fort Calder, Ohio</span></p>
    <p class="body" style="font-size:6px;margin-top:8px"><strong>Below is a partial listing of testimonials from attendees at a Founders Circle (FC) event provided by Colin Ashby, Chapter Learning Chair:</strong></p>
    <p class="quote">A very engaging, entertaining, and inspirational speaker who provided very useful information, strategies, and tips to apply to all my future negotiations.</p>
    <p class="quote">Thank you to FC Lakeshore for booking this speaker! I learned some things that I can address immediately and a lot material that I need to practice. Great session!</p>
    <p class="quote">Daniel was an outstanding speaker on the topic of negotiating! He was one of my favorite speakers ever! Daniel was a real 'teacher' versus other typical speakers who spend two hours bragging or promoting their book.</p>
    <p class="quote">Daniel was a very knowledgeable and well-prepared speaker who provided helpful tips and scripts throughout the entire presentation! I would love to learn more from this speaker.</p>
    <p class="body" style="color:var(--red);font-weight:700;font-size:6px;margin-top:6px">Colin Ashby, CEO and President</p>
  </div>
  <span class="more">Read More Testimonials - Click Here</span>
  <div class="closer">
    <p class="closer__org">Harborline Document Services</p>
    <p class="closer__role">Founders Circle (FC) Lakeshore<br>Learning Chair</p>
    <div class="dots"><i></i><i></i></div>
    <p class="closer__cta">Book Dealcraft Mentor® Daniel R. Whitcombe for Your Podcast</p>
    <div class="closer__row">
      <span class="contact"><svg width="9" height="7" viewBox="0 0 8 6"><rect x=".5" y=".5" width="7" height="5" fill="none" stroke="#fff" stroke-width=".8"/><path d="M.5 .5 4 3.3 7.5 .5" fill="none" stroke="#fff" stroke-width=".8"/></svg>daniel@whitcombe-mail.com</span>
      <span class="contact"><svg width="8" height="8" viewBox="0 0 10 10"><rect width="10" height="10" fill="#fff"/></svg>workloop.com/in/danielwhitcombe</span>
    </div>
    <p class="closer__phone"><svg width="11" height="11" viewBox="0 0 10 10"><circle cx="5" cy="5" r="4.3" fill="none" stroke="#fff"/><path d="M3.3 3c.3 1.8 1.5 3 3.4 3.6l.6-.9" fill="none" stroke="#fff"/></svg>555-014-2287</p>
    <div class="closer__site">
      <svg width="190" height="22" viewBox="0 0 190 22"><polygon points="10,0 190,0 190,22 0,22" fill="var(--white)"/></svg>
      <span class="contact" style="position:relative;color:var(--ink)"><svg width="7" height="7" viewBox="0 0 10 10"><circle cx="5" cy="5" r="4.3" fill="none" stroke="#333"/><path d="M.7 5h8.6M5 .7c-2.4 2.6-2.4 6 0 8.6M5 .7c2.4 2.6 2.4 6 0 8.6" fill="none" stroke="#333" stroke-width=".8"/></svg>www.dealcraftmentor.com</span>
    </div>
  </div>
</section>

</body>
</html>
```